Qorva - Web Design Rebrand for Talent Resourcing Company

I need a new brand for a customer based in Ireland.
The website currently: https://braddick.io/
Braddick repositioning themselves to be strategic talent resourcing and operational technology consultancy, Specialising in Life Sciences and Data Centres.
Essentially their USP:
They have lots of specialist manufacturing & automation resources that understand the Life Sciences Industry

Competitor websites:
https://vernhollow.com/ I really like the clarity on this site and the pink/yellow mix could be replaced with a green/blue mix for Braddick?
https://tulimark.com/ These are a big company so anything we could steal would be good 😊

They want:
• Fresh, sharp imagery
• Movement on the main page (Margot is obsessed with this lol) so may be video on some sections?
• The facility to upload CVs so similar to above.
• A page to show types of jobs available
• A page to show types of resource available from Braddick
• About us
• Sectors they operate in (includes Life Sciences, Food & Bev, Data Centres)

Target Market(s)

HR/Recruitment/Talent Acquisition/Operations Personnel in Life Sciences and Data Centres

Industry/Entity Type

Life Sciences and Data Centres

Number of Pages Required

1 page

Font styles to use
Sans Serif

Colors
0054AA
0677BA
7BADD7
CADEEF
E8F1F8
0094D4
00A9DD
6FCCEA
C7EBF8
E9F6FB
00AB8E
00BBA5
67D7C9
C6EFE9
E9F9F6

Requirements
Must have
• Brand Colour might be green/blue mix OR if another colour combo compelling
Nice to have
• Fresh, Sharp imagery. Movement on the main image (maybe partial video)

```html
<!DOCTYPE html>
<html lang="en">
<head>
<meta charset="utf-8">
<title>Braddick – Strategic Talent Resourcing</title>
<link href="https://fonts.googleapis.com/css2?family=Rubik:wght@500;600;700&family=Roboto:wght@400;500;700&display=swap" rel="stylesheet">
<style>
:root{
  --teal-dark:#0b5c73;
  --teal:#0a6e8c;
  --blue:#0094d4;
  --blue-bright:#00a9dd;
  --sky:#19a3d8;
  --ice:#e6f8fb;
  --ink:#1e1e1e;
  --text:#333;
  --muted:#555;
  --line:#cfcfcf;
  --white:#fff;
}
*{box-sizing:border-box;margin:0;padding:0}
html,body{width:1200px;height:3748px;overflow:hidden}
body{position:relative;background:var(--white);font-family:"Roboto",Arial,sans-serif;color:var(--text)}
.abs{position:absolute}
h1,h2,h3{font-family:"Rubik",Arial,sans-serif}

/* header */
.site-header{left:0;top:0;width:1200px;height:84px;background:var(--white)}
.brand{left:112px;top:14px;font-family:"Rubik",sans-serif;font-weight:700;font-size:46px;color:var(--teal)}
.nav{left:361px;top:32px;display:flex;gap:34px;font-size:15px;color:#333;letter-spacing:.2px}
.btn-login{left:960px;top:20px;width:128px;height:41px;border-radius:21px;background:linear-gradient(90deg,#0a6e8c,#0a8ec4);color:#fff;font-weight:700;font-size:15px;display:flex;align-items:center;justify-content:center;gap:10px}

/* hero */
.hero{left:0;top:84px;width:1200px;height:610px;background:
  linear-gradient(90deg,rgba(10,40,70,.55) 0%,rgba(10,40,70,0) 25%,rgba(10,40,70,0) 75%,rgba(10,40,70,.55) 100%),
  radial-gradient(ellipse at 50% 35%,#5cc3d8 0%,#2a84a8 30%,#124a78 62%,#0a1f3e 100%)}
.hero-title{left:0;top:228px;width:1200px;text-align:center;color:#fff;font-weight:700;font-size:43px;line-height:57px}
.hero-sub{left:0;top:416px;width:1200px;text-align:center;color:#fff;font-family:"Rubik",sans-serif;font-weight:500;font-size:25px}
.btn-pill{display:flex;align-items:center;justify-content:center;gap:10px;color:#fff;font-weight:700;font-size:15px;border-radius:20px;background:linear-gradient(90deg,#0a6e8c,#0a8ec4)}
.hero-cta{left:519px;top:474px;width:162px;height:38px}

/* about */
.about{left:0;top:694px;width:1200px;height:567px;background:var(--ice)}
.about-ring{left:117px;top:755px;width:444px;height:444px;border-radius:50%;border:4px solid var(--teal);border-right-color:var(--blue-bright);border-top-color:var(--blue-bright)}
.about-photo{left:131px;top:769px;width:416px;height:416px;border-radius:50%;background:radial-gradient(circle at 45% 40%,#3a8fd0,#163e78 60%,#0b1f44)}
.play{left:482px;top:1080px;width:46px;height:46px;border-radius:50%;background:#fff;box-shadow:0 2px 8px rgba(0,0,0,.2)}
.about-title{left:611px;top:774px;font-size:42px;font-weight:700;color:#222}
.about-copy{left:611px;top:828px;width:470px;font-size:15px;line-height:25.5px;color:#333;text-align:justify}
.about-copy p+p{margin-top:6px}
.about-cta{left:611px;top:1133px;width:163px;height:38px}

/* team */
.team-title{left:0;top:1340px;width:1200px;text-align:center;font-size:42px;font-weight:700;color:#222}
.team-intro{left:190px;top:1400px;width:820px;text-align:center;font-size:15px;line-height:26px;color:#333}
.featured{left:0;top:1488px;width:1200px;text-align:center;font-family:"Rubik",sans-serif;font-weight:600;font-size:20px;color:var(--sky)}
.card{width:299px;height:398px;border:1px solid var(--line);background:#fff}
.card-img{position:absolute;left:0;top:0;width:297px;height:190px}
.card h3{position:absolute;left:0;top:218px;width:100%;text-align:center;font-family:"Roboto",sans-serif;font-weight:500;font-size:17px;color:#222}
.card p{position:absolute;left:12px;top:248px;width:273px;text-align:center;font-size:14px;line-height:26px;color:#555}
.card .btn-outline{position:absolute;left:77px;top:332px;width:144px;height:35px;border:1.5px solid var(--sky);border-radius:18px;color:var(--sky);font-weight:500;font-size:15px;display:flex;align-items:center;justify-content:center}

/* resource */
.resource{left:0;top:2455px;width:1200px;height:355px;background:linear-gradient(180deg,#0a9fd8,#0aa6dc 60%,#12a8dd)}
.resource-title{left:0;top:2520px;width:1200px;text-align:center;color:#fff;font-size:42px;font-weight:700}
.stat{width:340px;text-align:center;color:#fff}
.stat-num{font-family:"Rubik",sans-serif;font-weight:700;font-size:60px;line-height:70px}
.stat-label{margin-top:22px;font-weight:700;font-size:15px}
.divider{width:1px;height:127px;background:rgba(255,255,255,.7);top:2608px}

/* sectors */
.sectors-title{left:0;top:2886px;width:1200px;text-align:center;font-size:42px;font-weight:700;color:#222}
.sector{width:300px;text-align:center}
.sector-img{width:190px;height:190px;border-radius:50%;margin:0 auto;border:4px solid #fff;box-shadow:0 4px 14px rgba(0,0,0,.25)}
.sector h3{margin-top:20px;font-family:"Roboto",sans-serif;font-weight:700;font-size:15px;color:#222}
.sector p{margin:8px auto 0;width:290px;font-size:14px;line-height:23px;color:#333}

/* footer */
.footer{left:0;top:3386px;width:1200px;height:362px;background:var(--teal-dark)}
.foot-h{font-family:"Rubik",sans-serif;font-weight:600;font-size:19px;color:var(--white)}
.contact-item{left:113px;display:flex;gap:14px;font-size:14px;line-height:22px;color:var(--white)}
.contact-item svg{flex:none;margin-top:3px}
.links{font-size:14px;line-height:31px;color:var(--white);list-style:none}
.email-field{left:719px;top:3497px;width:235px;height:44px;border-radius:22px;background:#fff;color:#888;font-size:11px;padding-left:22px;display:flex;align-items:center}
.btn-submit{left:969px;top:3497px;width:122px;height:44px;border-radius:22px;background:var(--blue-bright);color:#fff;font-weight:700;font-size:17px;display:flex;align-items:center;justify-content:center}
.consent{left:715px;top:3567px;font-size:13px;font-weight:500;display:flex;gap:8px;align-items:center;color:var(--white)}
.social{width:32px;height:32px;border-radius:50%;border:1.5px solid #fff;top:3606px}
.foot-rule{left:109px;top:3692px;width:979px;height:1px;background:rgba(255,255,255,.45)}
.copyright{left:0;top:3713px;width:1200px;text-align:center;font-size:13px;color:var(--white)}
</style>
</head>
<body>

<header class="abs site-header">
  <div class="abs brand">Braddick</div>
  <nav class="abs nav"><span>HOME</span><span>ABOUT US</span><span>TEAM</span><span>RESOURCE</span><span>SECTORS</span><span>CONTACT US</span></nav>
  <div class="abs btn-login">LOGIN
    <svg width="12" height="14" viewBox="0 0 12 14"><circle cx="6" cy="3.5" r="3.2" fill="#fff"/><path d="M0 14c0-4 2.5-6 6-6s6 2 6 6z" fill="#fff"/></svg>
  </div>
</header>

<section class="abs hero" role="img" aria-label="Data centre corridor lined with glowing server racks"></section>
<h1 class="abs hero-title">Strategic Talent<br>Resourcing and Operational<br>Technology Experts</h1>
<p class="abs hero-sub">Specialising in Life Sciences and Data Centres.</p>
<div class="abs btn-pill hero-cta">CONTACT US
  <svg width="14" height="14" viewBox="0 0 14 14"><circle cx="7" cy="7" r="7" fill="#fff"/><path d="M4 7h5M7 4.5 9.5 7 7 9.5" stroke="#0a6e8c" stroke-width="1.8" fill="none"/></svg>
</div>

<section class="abs about"></section>
<div class="abs about-ring"></div>
<div class="abs about-photo" role="img" aria-label="Engineer working on a laptop beside a server rack"></div>
<div class="abs play"><svg width="46" height="46" viewBox="0 0 46 46"><circle cx="23" cy="23" r="12" fill="#0a8ec4"/><path d="M20 17v12l10-6z" fill="#fff"/></svg></div>
<h2 class="abs about-title">About Us</h2>
<div class="abs about-copy">
  <p>Braddick is proud to be providing top-tier resources to the life sciences sector, specialising in delivering high-quality talent and solutions that enhance the capabilities and operational excellence of our customers.</p>
  <p>Ouroperational technology expertise and talent pool has evolved over the past decade with successful project delivery for numerous life sciences organisations, so we are uniquely positioned to understand and meet your requirements.</p>
  <p>We are focused on matching the dynamic needs of life sciences firms with skilled professionals, thereby driving innovation and growth in this critical sector across Ireland.</p>
</div>
<div class="abs btn-pill about-cta">READ MORE
  <svg width="14" height="14" viewBox="0 0 14 14"><circle cx="7" cy="7" r="7" fill="#fff"/><path d="M4 7h5M7 4.5 9.5 7 7 9.5" stroke="#0a6e8c" stroke-width="1.8" fill="none"/></svg>
</div>

<h2 class="abs team-title">Meet Our Team</h2>
<p class="abs team-intro">Braddick employees have a variety of skills and experience, but they all are professional, experienced in their field and enjoy the variety of working at different client sites over time. They get a feeling of success seeing a project through to completion, and are always willing to go the extra mile for our clients.</p>
<div class="abs featured">Featured Roles</div>

<article class="abs card" style="left:116px;top:1542px">
  <div class="card-img" role="img" aria-label="Worker with tablet in a warehouse aisle" style="background:linear-gradient(160deg,#7fc7e0,#2b6f9a 60%,#1b4a6e)"></div>
  <h3>Connected Worker</h3>
  <p>From supply chain systems to warehouse management discover why connected workers are the foundation of the factory</p>
  <div class="btn-outline">READ MORE</div>
</article>
<article class="abs card" style="left:451px;top:1542px">
  <div class="card-img" role="img" aria-label="Team reviewing charts on a laptop at a desk" style="background:linear-gradient(160deg,#e6f1f5,#a9c9d6 60%,#6d9fb3)"></div>
  <h3>Digital Strategy</h3>
  <p>In many cases this sets out a vision for the digital customer relationship based around the Halvern PACE layered</p>
  <div class="btn-outline">READ MORE</div>
</article>
<article class="abs card" style="left:785px;top:1542px">
  <div class="card-img" role="img" aria-label="Engineer drafting plans beside a hard hat" style="background:linear-gradient(160deg,#c7d6de,#7d9fb0 55%,#3f6a80)"></div>
  <h3>Infrastructure design</h3>
  <p>Infrastructure design for life sciences manufacturing operations can be complex. We have a lot of experience of designing</p>
  <div class="btn-outline">READ MORE</div>
</article>
<article class="abs card" style="left:116px;top:1972px">
  <div class="card-img" role="img" aria-label="Analyst monitoring security screens" style="background:linear-gradient(160deg,#2f7fa8,#123e60 60%,#0b2238)"></div>
  <h3>Resilience &amp; Security</h3>
  <p>Business continuity in manufacturing operations is critical – and quite complex. Braddick has strong specialist knowledge</p>
  <div class="btn-outline">READ MORE</div>
</article>
<article class="abs card" style="left:451px;top:1972px">
  <div class="card-img" role="img" aria-label="Hand touching a glowing tablet screen" style="background:linear-gradient(160deg,#8fd4e6,#3fa1c3 55%,#1f6f93)"></div>
  <h3>Application Rollout</h3>
  <p>eployment of software application to enable manufacturing operations can be complex and delicate We can help your</p>
  <div class="btn-outline">READ MORE</div>
</article>
<article class="abs card" style="left:785px;top:1972px">
  <div class="card-img" role="img" aria-label="Hand arranging wooden blocks with lifecycle symbols" style="background:linear-gradient(160deg,#dfe9ec,#a8c3c9 55%,#6d97a3)"></div>
  <h3>Lifecycle Planning</h3>
  <p>AIT Leaders are challenged with sustaining manufacturing operations using a vast array of hardware and software</p>
  <div class="btn-outline">READ MORE</div>
</article>

<section class="abs resource" role="img" aria-label="Faint laboratory glassware backdrop in blue"></section>
<h2 class="abs resource-title">Resource</h2>
<div class="abs stat" style="left:106px;top:2612px"><div class="stat-num">50+</div><div class="stat-label">Number skilled automation engineers</div></div>
<div class="abs divider" style="left:461px"></div>
<div class="abs stat" style="left:474px;top:2612px"><div class="stat-num">25+</div><div class="stat-label">Customers currently using Braddick</div></div>
<div class="abs divider" style="left:836px"></div>
<div class="abs stat" style="left:816px;top:2612px"><div class="stat-num">99%</div><div class="stat-label">Customer retention</div></div>

<h2 class="abs sectors-title">Our Sectors</h2>
<div class="abs sector" style="left:125px;top:2977px">
  <div class="sector-img" role="img" aria-label="Scientists working with a microscope in a lab" style="background:radial-gradient(circle at 45% 40%,#f2f5f7,#b9c8d2 65%,#7e93a2)"></div>
  <h3>Life Sciences</h3>
  <p>Lorem ipsum dolor sit amet, consectetur adipiscing elit, sed do eiusmod tempor incididunt ut labore et dolore magna aliqua. Ut enim ad minim veniam,</p>
</div>
<div class="abs sector" style="left:451px;top:2977px">
  <div class="sector-img" role="img" aria-label="Plated food and drinks on a table" style="background:radial-gradient(circle at 50% 45%,#e9a35a,#7a4322 60%,#2a1a12)"></div>
  <h3>Food &amp; Bev</h3>
  <p>Lorem ipsum dolor sit amet, consectetur adipiscing elit, sed do eiusmod tempor incididunt ut labore et dolore magna aliqua. Ut enim ad minim veniam,</p>
</div>
<div class="abs sector" style="left:775px;top:2977px">
  <div class="sector-img" role="img" aria-label="Server room aisle" style="background:radial-gradient(circle at 50% 50%,#cfd8e6,#4b5f86 55%,#1b2240)"></div>
  <h3>Data Centres</h3>
  <p>Lorem ipsum dolor sit amet, consectetur adipiscing elit, sed do eiusmod tempor incididunt ut labore et dolore magna aliqua. Ut enim ad minim veniam,</p>
</div>

<footer class="abs footer"></footer>
<h3 class="abs foot-h" style="left:113px;top:3448px">Contact Us</h3>
<div class="abs contact-item" style="top:3494px">
  <svg width="14" height="16" viewBox="0 0 14 16"><path d="M7 0a5.5 5.5 0 0 0-5.5 5.5C1.5 10 7 16 7 16s5.5-6 5.5-10.5A5.5 5.5 0 0 0 7 0z" fill="#fff"/><circle cx="7" cy="5.5" r="2" fill="#0b5c73"/></svg>
  <span>7575 Lorem ipsum dolor sit<br>consectetur adipiscing elit</span>
</div>
<div class="abs contact-item" style="top:3553px">
  <svg width="16" height="12" viewBox="0 0 16 12"><rect width="16" height="12" rx="1.5" fill="#fff"/><path d="M1 1.5 8 7l7-5.5" stroke="#0b5c73" stroke-width="1.5" fill="none"/></svg>
  <span>info@braddick.com</span>
</div>
<div class="abs contact-item" style="top:3588px">
  <svg width="15" height="15" viewBox="0 0 15 15"><path d="M3 0 5.5 3.5 4 5.5c1 2 3.5 4.5 5.5 5.5L11.5 9.5 15 12l-1.5 3C6 15 0 9 0 1.5z" fill="#fff"/></svg>
  <span>+1 555 014 2290</span>
</div>
<div class="abs contact-item" style="top:3624px">
  <svg width="15" height="15" viewBox="0 0 15 15"><rect x="0" y="4" width="15" height="10" rx="1" fill="#fff"/><rect x="3" y="0" width="9" height="5" fill="#fff"/><rect x="3" y="7" width="9" height="1.5" fill="#0b5c73"/><rect x="3" y="10" width="9" height="1.5" fill="#0b5c73"/></svg>
  <span>555 019 3374</span>
</div>

<h3 class="abs foot-h" style="left:393px;top:3448px">Links</h3>
<ul class="abs links" style="left:393px;top:3488px"><li>Home</li><li>About Us</li><li>Team</li><li>Resource</li><li>Sectors</li><li>Contact Us</li></ul>
<ul class="abs links" style="left:521px;top:3488px"><li>Terms &amp; Condition</li><li>Privacy Policy</li><li>Updates</li><li>Support</li><li>Contact</li></ul>

<h3 class="abs foot-h" style="left:714px;top:3448px">Subscribe for Updates</h3>
<div class="abs email-field">Emaill Address</div>
<div class="abs btn-submit">SUBMIT</div>
<div class="abs consent">
  <svg width="13" height="13" viewBox="0 0 13 13"><rect x=".75" y=".75" width="11.5" height="11.5" rx="2" stroke="#fff" stroke-width="1.5" fill="none"/><path d="M3 6.5 5.5 9 10 3.5" stroke="#fff" stroke-width="1.8" fill="none"/></svg>
  Yes, Please Contact me.
</div>
<div class="abs social" style="left:715px"></div>
<div class="abs social" style="left:758px"></div>
<div class="abs social" style="left:800px"></div>
<div class="abs foot-rule"></div>
<p class="abs copyright">© 2024&nbsp; Braddick&nbsp; |&nbsp; All Rights Reserved</p>

</body>
</html>
```